New Architectural Firm Business Cards

New Business card to compliment previous pixel forum logo (attached). Please design a business card that is simple, modern, creative....please do not use "symbols", simply the logo and associated graphics/text. The front should contain name/address/phone/email/web address (with graphics).....back should be 100% graphic design using the logo somehow. Hoping for a two color (black and yellow) design. full bleed design, no borders

Target Market(s)

Commercial Architecture Clients

Industry/Entity Type

Architecture

Contact Information for Business Card

Please design a business card that is simple, modern, creative....please do not use "symbols", simply the logo and associated graphics/text. The front should contain name/address/phone/email/web address (with graphics).....back should be 100% graphic design using the logo somehow

Font styles to use
Sans Serif

Colors
FFF300
FFF600
FEFA6F
FFFEC7
FFFEE8

Requirements
Must have
• Clean, Modern Design
Should not have
• Stock images or "icons"

```html
<!DOCTYPE html>
<html lang="en">
<head>
<meta charset="utf-8">
<title>pixel forum – business cards</title>
<link href="https://fonts.googleapis.com/css2?family=Montserrat:wght@400;500;700&display=swap" rel="stylesheet">
<style>
  :root {
    --yellow: #f7c600;
    --ink: #1d1d1d;
    --text-grey: #3a3a3a;
    --paper: #ffffff;
    --stage: #2a2a2c;
    --back-light: #8a8a8a;
    --back-dark: #0c0c0c;
  }
  * { margin: 0; padding: 0; box-sizing: border-box; }
  html, body {
    width: 1200px;
    height: 900px;
    overflow: hidden;
    background: var(--stage);
    font-family: "Montserrat", sans-serif;
  }
  .card {
    position: absolute;
    width: 620px;
    height: 354px;
    border-radius: 22px;
    overflow: hidden;
  }

  /* Back of card */
  .card--back {
    left: 60px;
    top: 80px;
    background: var(--back-dark);
  }
  .back-pattern {
    position: absolute;
    inset: 0;
    background: linear-gradient(200deg, var(--back-dark) 30%, #3c3c3c 70%, var(--back-light) 100%);
  }
  .back-brand {
    position: absolute;
    right: 40px;
    top: 38px;
    font-weight: 700;
    font-size: 22px;
    color: var(--yellow);
    letter-spacing: 0.5px;
  }

  /* Front of card */
  .card--front {
    left: 520px;
    top: 470px;
    background: var(--paper);
  }
  .front-brand {
    position: absolute;
    right: 44px;
    top: 62px;
    display: flex;
    align-items: center;
    gap: 14px;
  }
  .front-brand__square {
    width: 34px;
    height: 34px;
    background: var(--yellow);
  }
  .front-brand__name {
    font-weight: 700;
    font-size: 44px;
    color: var(--yellow);
    letter-spacing: -0.5px;
  }
  .contact {
    position: absolute;
    left: 44px;
    bottom: 40px;
    color: var(--text-grey);
  }
  .contact__name {
    font-weight: 700;
    font-size: 22px;
    color: var(--yellow);
    line-height: 1.1;
  }
  .contact__title {
    font-size: 12px;
    font-weight: 500;
    margin-bottom: 16px;
  }
  .contact__address {
    font-size: 12px;
    line-height: 1.35;
    margin-bottom: 16px;
  }
  .contact__list { list-style: none; }
  .contact__item {
    display: flex;
    align-items: center;
    gap: 8px;
    font-size: 12px;
    line-height: 1.5;
  }
  .contact__icon {
    width: 11px;
    height: 11px;
    fill: var(--yellow);
    flex: none;
  }
</style>
</head>
<body>

  <section class="card card--back" aria-label="Card back">
    <div class="back-pattern" role="img" aria-label="Repeating glossy brand pattern fading from grey to black"></div>
    <div class="back-brand">pixel forum</div>
  </section>

  <section class="card card--front" aria-label="Card front">
    <div class="front-brand">
      <span class="front-brand__square"></span>
      <span class="front-brand__name">pixel forum</span>
    </div>

    <div class="contact">
      <p class="contact__name">Daniel Reyes</p>
      <p class="contact__title">President</p>
      <p class="contact__address">48 Linden Court<br>Northfield NY 11900</p>
      <ul class="contact__list">
        <li class="contact__item">
          <svg class="contact__icon" viewBox="0 0 24 24" aria-hidden="true"><path d="M6.6 10.8a15.1 15.1 0 0 0 6.6 6.6l2.2-2.2a1 1 0 0 1 1-.25 11.4 11.4 0 0 0 3.6.57 1 1 0 0 1 1 1V20a1 1 0 0 1-1 1A17 17 0 0 1 3 4a1 1 0 0 1 1-1h3.5a1 1 0 0 1 1 1c0 1.25.2 2.45.57 3.57a1 1 0 0 1-.25 1z"/></svg>
          1-555-204-7391
        </li>
        <li class="contact__item">
          <svg class="contact__icon" viewBox="0 0 24 24" aria-hidden="true"><path d="M2 5h20v14H2z M2 5l10 8 10-8" fill-rule="evenodd"/><path d="M3 6l9 7 9-7" fill="none" stroke="#fff" stroke-width="1.6"/></svg>
          info@pixelforumstudio.com
        </li>
        <li class="contact__item">
          <svg class="contact__icon" viewBox="0 0 24 24" aria-hidden="true"><circle cx="12" cy="12" r="10"/><path d="M2 12h20M12 2c3 3 3 17 0 20M12 2c-3 3-3 17 0 20" fill="none" stroke="#fff" stroke-width="1.4"/></svg>
          www.pixelforumstudio.com
        </li>
      </ul>
    </div>
  </section>

</body>
</html>
```